Place holder for book called THE AUDACITY OF DAWN

I'm relying on your imaginative genius because I have no suggestions for you. Attached is a picture of the author when young if it will be of help. The only other info I can offer is that the author uses the alphabet as a theme.

Book info:
Title: THE AUDACITY OF DAWN
Author: ROSALIND MCARDLE

This is a memoir. It's a story of daring to hope when things seem hopeless, of problems when changing countries, of making success of dross. I'm looking for a design that is daring, eye-catching but promises hope. I hope it's not impossible.

Can you give me a place holder for the book to go onto my website and for pre-publicity? Then, in 6-9 months I'll pay another $150 for the completion of hardcover, paperback and ebook covers.

```html
<!DOCTYPE html>
<html lang="en">
<head>
<meta charset="utf-8">
<title>The Audacity of Dawn – Cover</title>
<link rel="stylesheet" href="https://fonts.googleapis.com/css2?family=Cinzel:wght@400;700&family=Lato:wght@700&display=swap">
<style>
  :root {
    --page-bg: #ffffff;
    --ink-black: #111111;
    --title-brown: #8a4519;
    --sky-top: #eadbd6;
    --sky-mid: #f8eedf;
    --glow: #fff8dc;
    --sun: #fffbe8;
    --haze: #f0d6a8;
    --amber: #d8923f;
    --ember: #b8601f;
    --earth: #5a3a1e;
    --field: #7b5a2e;
    --shadow: rgba(0, 0, 0, 0.18);
  }
  * { margin: 0; padding: 0; box-sizing: border-box; }
  html, body {
    width: 1200px;
    height: 1200px;
    overflow: hidden;
    background: var(--page-bg);
  }
  .stage {
    position: relative;
    width: 1200px;
    height: 1200px;
  }
  .book-cover {
    position: absolute;
    left: 290px;
    top: 110px;
    width: 620px;
    height: 980px;
    overflow: hidden;
    box-shadow: 0 18px 40px var(--shadow);
  }
  .cover-art {
    position: absolute;
    inset: 0;
    background:
      radial-gradient(ellipse 38% 20% at 68% 66%, var(--sun) 0%, rgba(255, 251, 232, 0.85) 40%, rgba(255, 251, 232, 0) 100%),
      radial-gradient(ellipse 55% 18% at 80% 84%, rgba(216, 146, 63, 0.85) 0%, rgba(216, 146, 63, 0) 100%),
      radial-gradient(ellipse 60% 16% at 15% 94%, rgba(90, 58, 30, 0.9) 0%, rgba(90, 58, 30, 0) 100%),
      radial-gradient(ellipse 60% 22% at 20% 12%, rgba(214, 190, 190, 0.55) 0%, rgba(214, 190, 190, 0) 100%),
      radial-gradient(ellipse 50% 25% at 85% 30%, rgba(240, 214, 168, 0.6) 0%, rgba(240, 214, 168, 0) 100%),
      linear-gradient(180deg,
        var(--sky-top) 0%,
        var(--sky-mid) 22%,
        var(--glow) 48%,
        var(--haze) 70%,
        var(--amber) 82%,
        var(--ember) 90%,
        var(--field) 95%,
        var(--earth) 100%);
  }
  .author-name {
    position: absolute;
    top: 26px;
    left: 0;
    right: 0;
    text-align: center;
    font-family: "Cinzel", serif;
    font-weight: 700;
    font-size: 44px;
    letter-spacing: 1px;
    color: var(--ink-black);
  }
  .title-block {
    position: absolute;
    top: 330px;
    left: 0;
    right: 0;
    text-align: center;
    color: var(--title-brown);
  }
  .title-lead {
    display: block;
    font-family: "Lato", sans-serif;
    font-weight: 700;
    font-size: 40px;
    letter-spacing: 1px;
    line-height: 1;
  }
  .title-main {
    display: block;
    font-family: "Cinzel", serif;
    font-weight: 400;
    font-size: 172px;
    line-height: 1;
    margin-top: 4px;
  }
</style>
</head>
<body>
  <main class="stage">
    <section class="book-cover">
      <div class="cover-art" role="img" aria-label="Photograph of two hands reaching up against a barbed wire fence at sunrise, with birds flying into a warm golden sky over a grassy field"></div>
      <h2 class="author-name">ROSALIND MCARDLE</h2>
      <h1 class="title-block">
        <span class="title-lead">the audacity of</span>
        <span class="title-main">DAWN</span>
      </h1>
    </section>
  </main>
</body>
</html>
```